KV HOLDING Business Cards

I need business cards for "KV Holding group LLC" doublesided... logo on the back (also include logo on front)
logo attached to project... i have jpg up..
Company Info:
418 East Marlow Avenue, Suite 7B
Chicago, Illinois 60617
facsimile 312-555-0188 (list fax, address, website on all cards.)
www.kvholdinggroup.example
Three different people on cards:
Dorian P. Kell, CPA MST
Principal
ofc 312-555-0142
mobile 312-555-0167
dorianpkell@kvholdinggroup.example
Marcus T. Brenholt, CPA MST
Principal
marcustbrenholt@kvholdinggroup.example
mobile 708-555-0119
ofc 312-555-0142
Nigel F Carrow
Principal
ofc 312-555-0142
no mobile
nigelfcarrow@kvholdinggroup.example
I have multiple projects listed.. see below:
Business cards for amber gate equity llc
letterhead
envelopes
Business cards for KV Holding LLC
letterhead
envelopes
Target Market(s)
rich people
Industry/Entity Type
Business
Look and feel

```html
<!DOCTYPE html>
<html lang="en">
<head>
<meta charset="utf-8">
<title>KV Holding Group LLC — Business Cards</title>
<link rel="stylesheet" href="https://fonts.googleapis.com/css2?family=Arimo:wght@700&family=Cinzel:wght@400&display=swap">
<style>
  :root {
    --paper: #ffffff;
    --canvas: #ffffff;
    --ink: #1a1a1a;
    --olive: #a8a334;
    --border: #222222;
  }
  * { margin: 0; padding: 0; box-sizing: border-box; }
  html, body {
    width: 1200px;
    height: 4062px;
    overflow: hidden;
    background: var(--canvas);
  }
  .sheet { position: relative; width: 1200px; height: 4062px; }

  .card {
    position: absolute;
    left: 137px;
    width: 1020px;
    height: 566px;
    background: var(--paper);
    border: 3px solid var(--border);
    border-radius: 40px;
    overflow: hidden;
  }

  /* ---------- front ---------- */
  .header-rule {
    position: absolute;
    left: 0;
    top: 128px;
    width: 730px;
    height: 4px;
    background: var(--olive);
  }
  .person-name {
    position: absolute;
    left: 52px;
    top: 26px;
    font-family: "Arimo", Arial, sans-serif;
    font-weight: 700;
    font-size: 44px;
    line-height: 52px;
    color: var(--ink);
    white-space: nowrap;
  }
  .person-title {
    position: absolute;
    right: 330px;
    top: 86px;
    font-family: "Arimo", Arial, sans-serif;
    font-weight: 700;
    font-size: 22px;
    line-height: 26px;
    color: var(--ink);
  }
  .front-wordmark {
    position: absolute;
    right: 28px;
    top: 108px;
    font-family: "Arimo", Arial, sans-serif;
    font-weight: 700;
    font-size: 20px;
    line-height: 24px;
    color: var(--ink);
    white-space: nowrap;
  }
  .contact {
    position: absolute;
    left: 0;
    width: 100%;
    font-family: "Cinzel", Georgia, serif;
    font-size: 27px;
    color: var(--ink);
  }
  .contact-row { position: relative; height: 38px; line-height: 38px; }
  .contact-label { position: absolute; right: 579px; }
  .contact-colon { position: absolute; left: 502px; }
  .contact-value { position: absolute; left: 573px; font-family: Georgia, "Times New Roman", serif; font-size: 28px; }
  .contact-email {
    position: absolute;
    left: 0;
    width: 100%;
    text-align: center;
    font-family: "Cinzel", Georgia, serif;
    font-size: 24px;
    line-height: 30px;
    color: var(--ink);
    letter-spacing: 0.5px;
  }

  /* ---------- back ---------- */
  .back-wordmark {
    position: absolute;
    left: 0;
    width: 100%;
    top: 300px;
    text-align: center;
    font-family: "Arimo", Arial, sans-serif;
    font-weight: 700;
    font-size: 56px;
    line-height: 66px;
    color: var(--ink);
    white-space: nowrap;
  }
  .back-address {
    position: absolute;
    left: 0;
    width: 100%;
    top: 410px;
    text-align: center;
    font-family: "Cinzel", Georgia, serif;
    font-size: 24px;
    line-height: 34px;
    color: var(--ink);
  }
  .back-web {
    position: absolute;
    left: 0;
    width: 100%;
    top: 500px;
    text-align: center;
    font-family: "Cinzel", Georgia, serif;
    font-size: 22px;
    line-height: 28px;
    color: var(--ink);
  }
</style>
</head>
<body>
<main class="sheet">

  <section class="card card-front" style="top:2px;">
    <div class="header-rule"></div>
    <div class="person-name">Dorian P. Kell, CPA MST</div>
    <div class="person-title">Principal</div>
    <div class="front-wordmark">KV Holding Group LLC</div>
    <div class="contact" style="top:366px;">
      <div class="contact-row"><span class="contact-label">OFC</span><span class="contact-colon">:</span><span class="contact-value">312-555-0142</span></div>
      <div class="contact-row"><span class="contact-label">MOBILE</span><span class="contact-colon">:</span><span class="contact-value">312-555-0167</span></div>
      <div class="contact-row"><span class="contact-label">FACSIMILE</span><span class="contact-colon">:</span><span class="contact-value">312-555-0188</span></div>
    </div>
    <div class="contact-email" style="top:508px;">dorianpkell@kvholdinggroup.example</div>
  </section>

  <section class="card card-back" style="top:628px;">
    <div class="back-wordmark">KV Holding Group LLC</div>
    <div class="back-address">418 East Marlow Avenue, Suite 7B<br>Chicago, Illinois 60617</div>
    <div class="back-web">www.kvholdinggroup.example</div>
  </section>

  <section class="card card-front" style="top:1235px;">
    <div class="header-rule"></div>
    <div class="person-name">Marcus T. Brenholt, CPA MST</div>
    <div class="person-title">Principal</div>
    <div class="front-wordmark">KV Holding Group LLC</div>
    <div class="contact" style="top:366px;">
      <div class="contact-row"><span class="contact-label">OFC</span><span class="contact-colon">:</span><span class="contact-value">312-555-0142</span></div>
      <div class="contact-row"><span class="contact-label">MOBILE</span><span class="contact-colon">:</span><span class="contact-value">708-555-0119</span></div>
      <div class="contact-row"><span class="contact-label">FACSIMILE</span><span class="contact-colon">:</span><span class="contact-value">312-555-0188</span></div>
    </div>
    <div class="contact-email" style="top:508px;">marcustbrenholt@kvholdinggroup.example</div>
  </section>

  <section class="card card-back" style="top:1863px;">
    <div class="back-wordmark">KV Holding Group LLC</div>
    <div class="back-address">418 East Marlow Avenue, Suite 7B<br>Chicago, Illinois 60617</div>
    <div class="back-web">www.kvholdinggroup.example</div>
  </section>

  <section class="card card-front" style="top:2470px;">
    <div class="header-rule"></div>
    <div class="person-name" style="left:190px;">Nigel F Carrow</div>
    <div class="person-title">Principal</div>
    <div class="front-wordmark">KV Holding Group LLC</div>
    <div class="contact" style="top:404px;">
      <div class="contact-row"><span class="contact-label">OFC</span><span class="contact-colon">:</span><span class="contact-value">312-555-0142</span></div>
      <div class="contact-row"><span class="contact-label">FACSIMILE</span><span class="contact-colon">:</span><span class="contact-value">312-555-0188</span></div>
    </div>
    <div class="contact-email" style="top:512px;">nigelfcarrow@kvholdinggroup.example</div>
  </section>

  <section class="card card-back" style="top:3105px;">
    <div class="back-wordmark">KV Holding Group LLC</div>
    <div class="back-address">418 East Marlow Avenue, Suite 7B<br>Chicago, Illinois 60617</div>
    <div class="back-web">www.kvholdinggroup.example</div>
  </section>

</main>
</body>
</html>
```